Business Card Design

Copper Willow is a cabin in Gatlinburg, Tennessee, near the Pale Ridge Hollow National Park. When our cabin was built, there was one thing more important than any other--peace. The front of our cabin is surrounded by woods. It has a huge deck with a swing, Adirondack chairs, and a love seat for relaxation. The back deck has a hot tub, a large round glass table for cocktails or dinner, and because we left no stone unturned, we have a telescope for stargazing. There are two master suites, each have a private bath with a large jetted tub, seperate shower, flat screen TV, and a door that leads to the back deck.

Industry/Entity Type

Business

Contact Information for Business Card

Copper Willow Vacation Rentals, LLC
817 Harlow Brook Pl.
Oakland, Ky 42159
Janet K. Wilcox, Owner/Manager
(270) 555.0184

```html
<!DOCTYPE html>
<html lang="en">
<head>
<meta charset="utf-8">
<title>Copper Willow Vacation Rentals — Business Card</title>
<link rel="stylesheet" href="https://fonts.googleapis.com/css2?family=Crimson+Text:wght@400;700&display=swap">
<style>
  :root {
    --backdrop: #2e2a28;
    --card-white: #f7f7f5;
    --ink: #1f1f1f;
    --accent-orange: #f07f2a;
    --brand-blue: #1e4fa8;
    --blue-top: #1f6fcf;
    --blue-bottom: #1d3f93;
    --card-shadow: rgba(0, 0, 0, 0.45);
  }
  * { margin: 0; padding: 0; box-sizing: border-box; }
  html, body {
    width: 1200px;
    height: 844px;
    overflow: hidden;
    background: var(--backdrop);
    font-family: "Crimson Text", Georgia, serif;
  }
  .stage {
    position: relative;
    width: 1200px;
    height: 844px;
  }
  .card {
    position: absolute;
    top: 262px;
    width: 540px;
    height: 320px;
    box-shadow: 0 10px 24px var(--card-shadow);
  }
  .card--front {
    left: 40px;
    background: var(--card-white);
  }
  .card--back {
    left: 620px;
    background: linear-gradient(160deg, var(--blue-top), var(--blue-bottom));
    display: flex;
    align-items: center;
    justify-content: center;
  }
  .brand {
    display: flex;
    align-items: center;
    gap: 10px;
    font-weight: 700;
    line-height: 1.1;
  }
  .brand__dot {
    flex: none;
    border-radius: 50%;
  }
  .card--front .brand {
    position: absolute;
    top: 50px;
    right: 36px;
    width: 250px;
    color: var(--brand-blue);
    font-size: 19px;
  }
  .card--front .brand__dot {
    width: 18px;
    height: 18px;
    background: var(--brand-blue);
  }
  .card--back .brand {
    width: 340px;
    color: var(--accent-orange);
    font-size: 28px;
  }
  .card--back .brand__dot {
    width: 24px;
    height: 24px;
    background: var(--accent-orange);
  }
  .contact {
    position: absolute;
    left: 40px;
    bottom: 30px;
    color: var(--ink);
    font-size: 15px;
    line-height: 1.35;
  }
  .contact__name {
    font-size: 26px;
    font-weight: 700;
    line-height: 1.1;
  }
  .contact__role {
    color: var(--accent-orange);
    font-size: 17px;
    margin-bottom: 22px;
  }
  .label, .contact__web { color: var(--accent-orange); }
  .gap { margin-left: 8px; }
</style>
</head>
<body>
<main class="stage">
  <section class="card card--front" aria-label="Business card front">
    <div class="brand">
      <span class="brand__dot" aria-hidden="true"></span>
      <span class="brand__name">Copper Willow Vacation Rentals, LLC</span>
    </div>
    <div class="contact">
      <p class="contact__name">Janet K. Wilcox</p>
      <p class="contact__role">Owner/Manager</p>
      <p class="contact__address">817 Harlow Brook Pl., Oakland, Ky 42159</p>
      <p class="contact__phones">
        <span class="label">T:</span>(270) 555.0184
      </p>
      <p class="contact__online">
        <span class="label">E:</span> info@youremail.com
        <span class="contact__web gap">www.yourweb.com</span>
      </p>
    </div>
  </section>

  <section class="card card--back" aria-label="Business card back">
    <div class="brand">
      <span class="brand__dot" aria-hidden="true"></span>
      <span class="brand__name">Copper Willow Vacation Rentals, LLC</span>
    </div>
  </section>
</main>
</body>
</html>
```